Announcement Flyer for Customers - Promoting new complaint handling system & communication channels

Our requirement is to communicate development of a new automated complaint handling system to our customers along with new communication mode/ channels to receive complaints. The idea was to be briefly and visually communicate this to all our customer.
What – New complaint handling system & New communication channel (Toll free, website, email, etc)
Why – Serve our customers & increase their satisfaction
How – New communication channel (Toll free, website, email, etc)
Our customers - We are a UAE based insurance company with various classes of businesses.
Insurance

```html
<!DOCTYPE html>
<html lang="en">
<head>
<meta charset="utf-8">
<title>VESTRA – Customer Care Channels</title>
<link href="https://fonts.googleapis.com/css2?family=Arimo:wght@400;700&display=swap" rel="stylesheet">
<style>
  :root {
    --backdrop: #d9dadc;
    --paper-top: #e9eef3;
    --paper-bottom: #ffffff;
    --purple: #7a12b8;
    --purple-deep: #5a1aa6;
    --navy: #1c1f7a;
    --navy-deep: #141866;
    --banner-light: #8ea0dc;
    --ink: #222222;
    --white: #ffffff;
  }
  * { box-sizing: border-box; margin: 0; padding: 0; }
  html, body { width: 1200px; height: 1200px; overflow: hidden; }
  body {
    background: var(--backdrop);
    font-family: "Arimo", Arial, sans-serif;
    color: var(--ink);
    position: relative;
  }
  .flyer {
    position: absolute;
    left: 180px; top: 70px;
    width: 840px; height: 1060px;
    background: linear-gradient(180deg, var(--paper-top) 0%, #f2f5f8 60%, var(--paper-bottom) 100%);
    overflow: hidden;
  }
  .rule-vertical {
    position: absolute;
    width: 3px;
    background: linear-gradient(180deg, var(--purple) 0%, var(--purple) 75%, rgba(122,18,184,0) 100%);
  }
  .rule-left { left: 72px; top: 110px; height: 800px; }
  .rule-right { left: 768px; top: 75px; height: 800px; }

  .hero {
    position: absolute;
    left: 105px; top: 95px;
    width: 615px; height: 300px;
    border: 6px solid var(--white);
    background: linear-gradient(90deg, var(--navy-deep) 0%, var(--navy) 50%, #3a4ab0 75%, var(--banner-light) 100%);
    box-shadow: 0 2px 6px rgba(0,0,0,0.15);
  }
  .hero-headline {
    position: absolute;
    left: 28px; top: 36px;
    color: var(--white);
    font-size: 29px;
    line-height: 34px;
    font-weight: 400;
  }
  .hero-photo {
    position: absolute;
    right: 0; top: 0;
    width: 250px; height: 100%;
    background: linear-gradient(90deg, rgba(49,80,168,0) 0%, #3a58b4 40%, #6f86cf 100%);
  }
  .accent-band {
    position: absolute;
    left: 20px; top: 330px;
    width: 820px; height: 46px;
    background: linear-gradient(90deg, rgba(122,18,184,0.85) 0%, rgba(122,18,184,0.7) 100%);
  }

  .prompt-bar {
    position: absolute;
    left: 125px; top: 445px;
    width: 610px; height: 34px;
    background: var(--purple);
    color: var(--white);
    font-weight: 700;
    font-size: 15px;
    line-height: 34px;
    text-align: center;
  }
  .options-title {
    position: absolute;
    left: 0; width: 840px; top: 510px;
    text-align: center;
    color: var(--purple);
    font-size: 28px;
    font-weight: 400;
  }

  .channels {
    position: absolute;
    left: 130px; top: 575px;
    width: 600px; height: 200px;
    display: flex;
  }
  .channel {
    flex: 1;
    background: var(--white);
    text-align: center;
    padding-top: 16px;
    box-shadow: 0 3px 8px rgba(0,0,0,0.10);
    position: relative;
  }
  .channel + .channel { border-left: 3px solid var(--purple); }
  .channel-label { font-size: 15px; }
  .channel-icon {
    width: 78px; height: 78px;
    margin: 14px auto 12px;
    border-radius: 50%;
    background: linear-gradient(135deg, var(--purple) 0%, var(--purple-deep) 50%, var(--navy) 100%);
    display: flex; align-items: center; justify-content: center;
  }
  .channel-icon svg { width: 40px; height: 40px; }
  .channel-number { font-size: 30px; line-height: 32px; }
  .channel-note { font-size: 14px; }
  .channel-detail { font-size: 14px; line-height: 20px; }

  .tagline {
    position: absolute;
    left: 0; width: 840px; top: 795px;
    text-align: center;
    color: var(--purple);
    font-size: 28px;
  }
  .brand-name {
    position: absolute;
    left: 110px; top: 925px;
    font-size: 68px;
    font-weight: 400;
    color: var(--navy);
    letter-spacing: 2px;
  }
  .address {
    position: absolute;
    right: 80px; top: 905px;
    text-align: right;
    font-size: 15px;
    line-height: 22px;
    font-style: normal;
  }
</style>
</head>
<body>
  <main class="flyer">
    <div class="rule-vertical rule-left"></div>
    <div class="rule-vertical rule-right"></div>

    <section class="hero">
      <h1 class="hero-headline">It’s our job<br>to make every<br>important aspect of<br>customer experience<br>a little bit better.</h1>
      <div class="hero-photo" role="img" aria-label="Photo of a smiling customer service agent wearing a headset, giving a thumbs up"></div>
    </section>
    <div class="accent-band" role="img" aria-label="Purple decorative striped band crossing the banner"></div>

    <p class="prompt-bar">Get in touch with us if you have encountered a problem or have any concern.</p>
    <h2 class="options-title">Here's are the options</h2>

    <section class="channels">
      <div class="channel">
        <p class="channel-label">Call us on</p>
        <div class="channel-icon">
          <svg viewBox="0 0 24 24"><path fill="#fff" d="M6.6 10.8a15 15 0 0 0 6.6 6.6l2.2-2.2a1 1 0 0 1 1-.25 11.4 11.4 0 0 0 3.6.57 1 1 0 0 1 1 1V20a1 1 0 0 1-1 1A17 17 0 0 1 3 4a1 1 0 0 1 1-1h3.5a1 1 0 0 1 1 1c0 1.25.2 2.45.57 3.57a1 1 0 0 1-.25 1z"/></svg>
        </div>
        <p class="channel-number">800 2 417</p>
        <p class="channel-note">Toll Free</p>
      </div>
      <div class="channel">
        <p class="channel-label">Send us an Email on</p>
        <div class="channel-icon">
          <svg viewBox="0 0 24 24"><rect x="3" y="6" width="18" height="12" fill="#fff"/><path d="M3 6l9 7 9-7M3 18l7-6M21 18l-7-6" stroke="#5a1aa6" stroke-width="1.2" fill="none"/></svg>
        </div>
        <p class="channel-detail">care@vestradubai.com</p>
      </div>
      <div class="channel">
        <p class="channel-label">Log on to our websites</p>
        <div class="channel-icon">
          <svg viewBox="0 0 24 24" fill="none" stroke="#fff" stroke-width="1.6"><circle cx="12" cy="12" r="9"/><ellipse cx="12" cy="12" rx="4" ry="9"/><path d="M3 12h18M5 7.5h14M5 16.5h14"/></svg>
        </div>
        <p class="channel-detail">www.vestradubai.com<br>www.vestragulf.com<br>www.vestramiddleeast.com</p>
      </div>
    </section>

    <p class="tagline">An initiative to serve you better</p>

    <p class="brand-name">VESTRA</p>
    <address class="address">Harbor View Street<br>Crescent Trade Bldg.<br>Dubai, UAE</address>
  </main>
</body>
</html>
```